Business cards for the RL Group

We are looking for a template for our new business cards for our company that we can edit ourselves.
You will find our company colors in the logo. the logo on the back and on the front
first name Last Name
position
E-mail address
mobile number
landline number
Companies we have 2 RL Sicherheit GmbH and RL Services GmbH
address
Lindenbergweg 42
22459 Hamburg
www.rlgruppe-nord.de

Something modern, simple but professional

if you have any questions, bring it on.

Sicherheit

Steht in der Beschreibung

F0912C
F2A743
F7CA91
FBE8D2
FDF5EE

• recognition value
• professional
• Playful

```html
<!DOCTYPE html>
<html lang="de">
<head>
<meta charset="utf-8">
<title>RL Gruppe – Visitenkarten</title>
<link href="https://fonts.googleapis.com/css2?family=Roboto:wght@400;500;700&display=swap" rel="stylesheet">
<style>
  :root {
    --stage: #1b1b1b;
    --card-dark: #424242;
    --card-light: #ffffff;
    --brand-orange: #f0912c;
    --ink-grey: #4a4a4a;
    --mark-grey: #8c8c8c;
    --text-light: #ffffff;
    --text-soft: #e4e4e4;
  }
  * { box-sizing: border-box; margin: 0; padding: 0; }
  html, body {
    width: 1200px; height: 800px; overflow: hidden;
    background: var(--stage);
    font-family: "Roboto", Arial, sans-serif;
  }
  .stage {
    position: relative; width: 1200px; height: 800px;
  }
  .card {
    position: absolute; left: 320px;
    width: 560px; height: 320px;
    overflow: hidden;
  }
  /* Back side */
  .card--back { top: 50px; background: var(--card-dark); }
  .back-brand {
    position: absolute; top: 105px; left: 0; width: 100%;
    text-align: center;
    font-size: 54px; font-weight: 700; letter-spacing: 1px;
    color: var(--mark-grey);
  }
  .back-web {
    position: absolute; bottom: 44px; left: 0; width: 100%;
    text-align: center;
    font-size: 12px; letter-spacing: 6px;
    color: var(--text-light);
  }
  /* Front side */
  .card--front { top: 420px; background: var(--card-light); }
  .front-shape { position: absolute; inset: 0; }
  .front-brand {
    position: absolute; top: 46px; left: 0; width: 100%;
    display: flex; justify-content: center; align-items: center; gap: 10px;
  }
  .front-brand__dot {
    width: 16px; height: 16px; background: var(--brand-orange);
  }
  .front-brand__name {
    font-size: 40px; font-weight: 700; color: var(--ink-grey);
  }
  .contact {
    position: absolute; top: 204px; left: 236px;
    display: flex; align-items: stretch; gap: 12px;
    color: var(--text-light);
  }
  .contact__person { text-align: right; white-space: nowrap; }
  .contact__name { font-size: 17px; font-weight: 700; line-height: 20px; }
  .contact__role { font-size: 12px; color: var(--text-soft); line-height: 15px; margin-bottom: 8px; }
  .contact__address { font-size: 11px; line-height: 14px; color: var(--text-soft); }
  .contact__divider { width: 1px; background: var(--text-soft); }
  .contact__lines { list-style: none; font-size: 11px; line-height: 17px; color: var(--text-soft); white-space: nowrap; }
  .contact__lines li { display: flex; align-items: center; gap: 6px; }
  .contact__lines svg { width: 10px; height: 10px; fill: var(--text-light); flex: none; }
</style>
</head>
<body>
<main class="stage">

  <section class="card card--back" aria-label="Rückseite">
    <div class="back-brand">RL Gruppe</div>
    <div class="back-web">www.rlgruppe-nord.de</div>
  </section>

  <section class="card card--front" aria-label="Vorderseite">
    <svg class="front-shape" viewBox="0 0 560 320" width="560" height="320" aria-hidden="true">
      <path d="M58 320 C168 196 326 130 560 110 L560 119 C330 140 182 206 72 320 Z" fill="var(--brand-orange)"/>
      <path d="M72 320 C182 206 330 140 560 119 L560 320 Z" fill="var(--card-dark)"/>
    </svg>

    <div class="front-brand">
      <span class="front-brand__dot"></span>
      <span class="front-brand__name">RL Gruppe</span>
    </div>

    <div class="contact">
      <div class="contact__person">
        <div class="contact__name">Jonas Berger</div>
        <div class="contact__role">President</div>
        <div class="contact__address">Lindenbergweg 42<br>22459 Hamburg</div>
      </div>
      <div class="contact__divider"></div>
      <ul class="contact__lines">
        <li><svg viewBox="0 0 10 10"><path d="M2 0.5 L3.6 2.6 L2.7 3.6 C3.3 5 4.9 6.6 6.4 7.3 L7.4 6.4 L9.5 8 L8.3 9.5 C4.5 9 1 5.5 0.5 1.7 Z"/></svg>040-318-2264</li>
        <li><svg viewBox="0 0 10 10"><path d="M3 0 H7 A1 1 0 0 1 8 1 V9 A1 1 0 0 1 7 10 H3 A1 1 0 0 1 2 9 V1 A1 1 0 0 1 3 0 Z M3 1.5 V8 H7 V1.5 Z"/></svg>0171-529-4830</li>
        <li><svg viewBox="0 0 10 10"><path d="M0 2 H10 V8 H0 Z M0.8 2.6 L5 5.6 L9.2 2.6" fill="none" stroke="#fff" stroke-width="1"/></svg>j.berger@rlgruppe-nord.de</li>
        <li><svg viewBox="0 0 10 10"><circle cx="5" cy="5" r="4.5"/></svg>www.rlgruppe-nord.de</li>
      </ul>
    </div>
  </section>

</main>
</body>
</html>
```